Lantern Vigor
Basketball Fitness Training
Lantern Vigor -
Creative Brief
Modern
Doran Fisk
Health and Fitness Coach
tavmirlo@quillpost.example
www.lanternvigor.example
Youth Development Clinics Private 1 on 1 Sessions Executive Training Women's Fitness Cross Training

```html
<!DOCTYPE html>
<html lang="en">
<head>
<meta charset="utf-8">
<title>Lantern Vigor – Business Card</title>
<link rel="stylesheet" href="https://fonts.googleapis.com/css2?family=Archivo+Black&family=PT+Serif:ital,wght@1,700&family=Arimo:wght@400;700&display=swap">
<style>
  :root {
    --backdrop: #e9e6e1;
    --card: #ffffff;
    --ink: #111111;
    --name-blue: #1f4a9c;
    --accent-orange: #e0541b;
    --ball-orange: #e8561a;
    --placeholder-tone: #ecdccb;
    --contact-grey: #555555;
    --icon-grey: #3a4a6a;
  }
  * { box-sizing: border-box; margin: 0; padding: 0; }
  html, body {
    width: 1200px; height: 780px; overflow: hidden;
    background: var(--backdrop);
  }
  .card {
    position: absolute; left: 60px; top: 75px;
    width: 1080px; height: 630px;
    background: var(--card);
    border-radius: 40px;
    overflow: hidden;
    box-shadow: 0 6px 18px rgba(0,0,0,0.18);
  }
  .brand {
    position: absolute; left: 58px; top: 132px;
  }
  .brand-name {
    font-family: "Archivo Black", sans-serif;
    font-size: 62px; line-height: 1;
    color: var(--ink);
    letter-spacing: 0.5px;
  }
  .brand-tagline {
    font-family: "Archivo Black", sans-serif;
    font-size: 25px; line-height: 1;
    color: var(--ink);
    margin-top: 6px;
    margin-left: 32px;
  }
  .arm-illustration {
    position: absolute; left: 40px; top: 240px;
    width: 540px; height: 110px;
  }
  .feature-ball {
    position: absolute; left: 620px; top: -90px;
    width: 520px; height: 520px;
  }
  .contact-block {
    position: absolute; left: 62px; top: 408px;
  }
  .person-name {
    font-family: "PT Serif", serif;
    font-style: italic; font-weight: 700;
    font-size: 38px; line-height: 1;
    color: var(--name-blue);
  }
  .person-role {
    font-family: "Arimo", sans-serif;
    font-size: 26px; line-height: 1.2;
    color: var(--accent-orange);
    margin-top: 6px;
  }
  .contact-list {
    list-style: none; margin-top: 30px;
    font-family: "Arimo", sans-serif;
    font-size: 22px; color: var(--contact-grey);
  }
  .contact-list li {
    display: flex; align-items: center; gap: 16px;
    margin-bottom: 16px;
  }
  .contact-icon { width: 22px; height: 22px; flex: none; }
</style>
</head>
<body>
  <main class="card">
    <div class="brand">
      <div class="brand-name">Lantern Vigor</div>
      <div class="brand-tagline">Basketball Fitness Training</div>
    </div>

    <svg class="arm-illustration" viewBox="0 0 540 110" role="img" aria-label="Illustration area: outstretched arm holding a basketball">
      <rect x="0" y="0" width="540" height="110" rx="8" fill="var(--placeholder-tone)"/>
    </svg>

    <svg class="feature-ball" viewBox="0 0 520 520" role="img" aria-label="Illustration area: large basketball">
      <circle cx="260" cy="260" r="258" fill="var(--ball-orange)"/>
    </svg>

    <section class="contact-block">
      <div class="person-name">Doran Fisk</div>
      <div class="person-role">Health and Fitness Coach</div>
      <ul class="contact-list">
        <li>
          <svg class="contact-icon" viewBox="0 0 24 24" aria-hidden="true">
            <circle cx="12" cy="12" r="4" fill="none" stroke="var(--icon-grey)" stroke-width="2.4"/>
            <path d="M16 8v5.5a2.5 2.5 0 0 0 5 0V12a9 9 0 1 0-4 7.5" fill="none" stroke="var(--icon-grey)" stroke-width="2.4"/>
          </svg>
          <span>tavmirlo@quillpost.example</span>
        </li>
        <li>
          <svg class="contact-icon" viewBox="0 0 24 24" aria-hidden="true">
            <circle cx="12" cy="12" r="10" fill="none" stroke="var(--icon-grey)" stroke-width="2"/>
            <ellipse cx="12" cy="12" rx="4.5" ry="10" fill="none" stroke="var(--icon-grey)" stroke-width="1.6"/>
            <path d="M2 12h20M4 7h16M4 17h16" stroke="var(--icon-grey)" stroke-width="1.4"/>
          </svg>
          <span>www.lanternvigor.example</span>
        </li>
      </ul>
    </section>
  </main>
</body>
</html>
```